8" x 11" One Page Flyer for Fence Installation Company

We are looking to promote our business with a new flyer that would be handed out in person to people or put at their mailbox/door at their homes. The flyer needs to be creative and attention-grabbing. I have attached some of our previous flyers and our website information. Do not call or email regarding the flyer. We want the flyer to look professional but also friendly. One page, NOT folded. You can use images from our website at www.MyBraxtonYard.com or our Facebook page at www.Facebook.com/HollowbrookRailsBKT. We are flexible with what photos you can use but there must be photos of OUR fences on the flyer. More photos specifically can also be provided. Colors need to be suitable for a flyer printed on canary yellow in color paper OR white paper.

Target Market(s)

Homeowners that need a new fence

Industry/Entity Type

Construction

Font styles to use
Sans Serif
Other font styles liked:
• HD Colton

Colors
0054AA
0677BA
7BADD7
CADEEF
E8F1F8
0094D4
00A9DD
6FCCEA
C7EBF8
E9F6FB

Requirements
Must have
• Our fence photos - mostly wood fence photos (different designs), SIZE SHOULD BE LETTER SIZE 8" x 11"
Nice to have
• A nice bible verse featured at the bottom of the flyer.
Should not have
• DO NOT COPY THE WEBSITE FORMAT, I WANT SOMETHING UNIQUE. Other people's fence photos, they must all come from our website or facebook page

```html
<!DOCTYPE html>
<html lang="en">
<head>
<meta charset="utf-8">
<title>Hollowbrook Rails – Fence Flyer</title>
<link rel="stylesheet" href="https://fonts.googleapis.com/css2?family=Roboto:ital,wght@0,300;0,400;0,500;0,700;0,900;1,400;1,500;1,700&display=swap">
<style>
  :root {
    --page-bg: #e4e4e4;
    --paper: #f4f4f4;
    --ink: #111111;
    --brown: #4a2e1f;
    --blue-bright: #0094d4;
    --blue-mid: #0677ba;
    --blue-deep: #0054aa;
    --navy: #0b3f94;
    --sky: #6fccea;
    --pale: #cadeef;
    --panel: #e1ebf3;
    --white: #ffffff;
  }
  * { margin: 0; padding: 0; box-sizing: border-box; }
  html, body { width: 1135px; height: 1200px; overflow: hidden; }
  body { background: var(--page-bg); font-family: "Roboto", Arial, sans-serif; position: relative; }

  .flyer {
    position: absolute; left: 161px; top: 30px;
    width: 812px; height: 1140px;
    background: var(--paper);
    overflow: hidden;
    box-shadow: 0 12px 30px rgba(0,0,0,.25);
  }
  .abs { position: absolute; }

  /* header */
  .brand-mark { left: 56px; top: 56px; width: 84px; height: 84px; background: var(--brown); }
  .brand-name { left: 161px; top: 50px; font-size: 33px; font-weight: 700; color: var(--blue-mid); letter-spacing: .5px; }
  .brand-phone { left: 161px; top: 88px; font-size: 34px; font-weight: 900; color: var(--ink); letter-spacing: 1px; }
  .brand-tagline { left: 161px; top: 134px; font-size: 11px; font-weight: 700; color: var(--ink); }
  .contact { right: 56px; top: 80px; text-align: right; font-size: 16.5px; font-weight: 500; color: var(--brown); line-height: 24.5px; }

  /* photos */
  .photo { position: absolute; }
  .photo-rail   { left: 0;   top: 165px; width: 378px; height: 238px; background: linear-gradient(135deg,#3d5a2c,#b98c4a 60%,#d8b06b); }
  .photo-field  { left: 385px; top: 165px; width: 213px; height: 120px; background: linear-gradient(180deg,#7fa9d9 0%,#a88a72 40%,#8f7a5a 100%); }
  .photo-iron   { left: 606px; top: 165px; width: 206px; height: 161px; background: linear-gradient(180deg,#d9dde2 0%,#7e9a56 55%,#4f7a2e 100%); }
  .photo-yard   { left: 385px; top: 292px; width: 213px; height: 212px; background: linear-gradient(160deg,#6f9a48 0%,#c9b48c 55%,#e2cfa4 100%); }
  .photo-privacy{ left: 606px; top: 332px; width: 206px; height: 172px; background: linear-gradient(180deg,#9fb2c8 0%,#5b7a3c 45%,#b48d62 100%); }

  /* headline panel */
  .headline-panel {
    left: 0; top: 404px; width: 511px; height: 197px;
    background: var(--panel);
    border-radius: 0 98px 98px 0;
    z-index: 2;
  }
  .headline-1 { left: 61px; top: 418px; font-size: 66px; font-weight: 900; color: var(--blue-bright); z-index: 3; }
  .headline-2 { left: 61px; top: 486px; font-size: 66px; font-weight: 900; color: var(--navy); z-index: 3; }
  .headline-sub { left: 61px; top: 561px; font-size: 18px; font-style: italic; font-weight: 500; color: var(--brown); z-index: 3; }

  /* blue section */
  .blue-band {
    left: 0; top: 504px; width: 812px; height: 618px;
    background: linear-gradient(180deg, var(--blue-mid) 0%, #0a5fb2 50%, var(--blue-deep) 100%);
    z-index: 1;
  }
  .blue-content { z-index: 3; }

  .why { right: 580px; top: 636px; text-align: right; font-size: 44px; font-weight: 300; color: var(--pale); line-height: 51px; }
  .benefits-title { left: 264px; top: 651px; font-size: 25px; font-style: italic; font-weight: 500; color: var(--sky); }
  .benefits { list-style: none; font-size: 15px; color: var(--white); line-height: 23.3px; }
  .benefits li::before { content: "•"; margin-right: 6px; }
  .benefits-left { left: 257px; top: 697px; }
  .benefits-right { left: 507px; top: 697px; }

  .showroom-ring { left: 67px; top: 818px; width: 168px; height: 168px; }
  .showroom-badge {
    left: 75px; top: 826px; width: 152px; height: 152px; border-radius: 50%;
    background: var(--pale);
    display: flex; align-items: center; justify-content: center; text-align: center;
    font-size: 20px; font-style: italic; font-weight: 500; line-height: 25px; color: var(--brown);
  }
  .hours-line { left: 262px; font-size: 17px; color: var(--white); }
  .hours-line.strong { font-weight: 500; font-size: 18px; }
  .rule { left: 226px; width: 495px; height: 0; border-top: 1px solid var(--pale); }
  .rule.dashed { border-top-style: dashed; }
  .address { left: 262px; top: 949px; display: flex; align-items: center; gap: 8px; font-size: 17px; color: var(--white); }

  .verse { left: 0; width: 812px; top: 1018px; text-align: center; font-size: 17px; line-height: 24px; color: var(--pale); }
  .verse-ref { display: block; margin-top: 6px; font-style: italic; color: var(--sky); font-size: 18px; }
</style>
</head>
<body>
<main class="flyer">
  <header>
    <div class="abs brand-mark" aria-hidden="true"></div>
    <div class="abs brand-name">Hollowbrook Rails</div>
    <div class="abs brand-phone">555-014-2290</div>
    <div class="abs brand-tagline">"Because Good Fences Make Good Neighbors"</div>
    <address class="abs contact" style="font-style:normal">
      555-014-2290<br>
      www.MyBraxtonYard.com<br>
      office@mybraxtonyard.com
    </address>
  </header>

  <section class="gallery">
    <div class="photo photo-rail" role="img" aria-label="Close-up of a wooden split-rail fence with wire mesh and a company sign on the post"></div>
    <div class="photo photo-field" role="img" aria-label="Long three-rail wooden fence beside a brick house"></div>
    <div class="photo photo-iron" role="img" aria-label="Black aluminum fence around a backyard lawn"></div>
    <div class="photo photo-yard" role="img" aria-label="Wooden picket privacy fence enclosing a backyard patio"></div>
    <div class="photo photo-privacy" role="img" aria-label="Tall wooden privacy fence lined with rose bushes"></div>
  </section>

  <div class="abs headline-panel"></div>
  <h1 class="abs headline-1">We Build</h1>
  <div class="abs headline-2">Fences....</div>
  <p class="abs headline-sub">and we would love to build your fence too!</p>

  <div class="abs blue-band"></div>

  <section class="blue-content">
    <h2 class="abs why blue-content">Why<br>Choose<br>Us?</h2>
    <h3 class="abs benefits-title blue-content">Beautiful, professionally installed fences</h3>
    <ul class="abs benefits benefits-left blue-content">
      <li>Free Estimates</li>
      <li>Professional Installation</li>
      <li>Concrete in EVERY Post</li>
      <li>HOA Submission Assistance</li>
    </ul>
    <ul class="abs benefits benefits-right blue-content">
      <li>Lifetime Workmanship Warranty</li>
      <li>Experienced Installation Teams</li>
      <li>Quality Workmanship &amp; Materials</li>
      <li>FREE Gate Adjustments for LIFE</li>
    </ul>

    <svg class="abs showroom-ring blue-content" viewBox="0 0 168 168" aria-hidden="true">
      <path d="M84 2 A82 82 0 0 1 84 166" fill="none" stroke="#0b3f94" stroke-width="3"/>
    </svg>
    <div class="abs showroom-badge blue-content">Visit our<br>indoor &amp;<br>outdoor<br>showroom!</div>

    <p class="abs hours-line blue-content" style="top:835px">Our outdoor showroom is open 24/7,</p>
    <div class="abs rule blue-content" style="top:863px"></div>
    <p class="abs hours-line blue-content" style="top:872px">while our indoor showroom and office is open</p>
    <div class="abs rule dashed blue-content" style="top:899px"></div>
    <p class="abs hours-line strong blue-content" style="top:909px">Monday - Thurs | 9AM - 3PM, Friday 9AM - 1PM</p>
    <div class="abs rule blue-content" style="top:939px"></div>
    <p class="abs address blue-content">
      <svg width="18" height="24" viewBox="0 0 18 24" aria-hidden="true">
        <path d="M9 0C4 0 0 4 0 9c0 6.5 9 15 9 15s9-8.5 9-15C18 4 14 0 9 0z" fill="#6fccea"/>
        <circle cx="9" cy="9" r="3.5" fill="#0677ba"/>
      </svg>
      418 Millpond Rd Braxton, NC 28000
    </p>

    <p class="abs verse blue-content">
      May the God of hope fill you with all joy and peace as you trust in Him, so<br>
      that you may overflow with hope by the power of the Holy Spirit.
      <span class="verse-ref">Romans 15:13 (NIV)</span>
    </p>
  </section>
</main>
</body>
</html>
```